Marlow Naturopathics business card design

Using the marlow logo designed, we would like that incorporated into a business card. A colour scheme which works with the logo and lists the following business details:

Dennis Marlow - Naturopath
Level 1, 58 Torvane Street
Calder Bay NSW
(02) 4391 7084
www.dennismarlowhealth-example.com

We would also like space on the back of the card for next appointment times.

Target Market(s)

Anyone looking to improve their health

Industry/Entity Type

Business

Requirements
Must have
• Marlow Naturopathics logo, business details.
Nice to have
• Good colour schemes, attractive, eye-catching features that are easy to read.

```html
<!DOCTYPE html>
<html lang="en">
<head>
<meta charset="utf-8">
<title>Marlow Naturopathics – Business Card</title>
<link rel="stylesheet" href="https://fonts.googleapis.com/css2?family=Didact+Gothic&family=Montserrat:wght@700&display=swap">
<style>
  :root {
    --canvas: #e9ecef;
    --blue-deep: #123f86;
    --blue-mid: #1e62b0;
    --blue-light: #3a8fd3;
    --card-white: #f7f7f5;
    --ink: #5a5a5a;
    --ink-soft: #8a8a8a;
    --on-blue: #eef4fb;
    --on-blue-soft: #c9dcf2;
    --rule: #b5b5b5;
  }
  * { box-sizing: border-box; margin: 0; padding: 0; }
  html, body { width: 1200px; height: 800px; overflow: hidden; }
  body {
    background: var(--canvas);
    font-family: "Didact Gothic", "Century Gothic", sans-serif;
    display: flex;
    align-items: center;
    justify-content: center;
    gap: 60px;
  }
  .card {
    width: 520px;
    height: 316px;
    border-radius: 4px;
    box-shadow: 0 10px 28px rgba(0,0,0,.18);
    position: relative;
    overflow: hidden;
  }

  /* Front */
  .card-front {
    background: linear-gradient(135deg, var(--blue-deep) 0%, var(--blue-mid) 55%, var(--blue-light) 100%);
    color: var(--on-blue);
  }
  .front-brand {
    position: absolute;
    left: 60px; top: 86px;
    display: flex;
    align-items: center;
    gap: 14px;
    white-space: nowrap;
  }
  .brand-dot {
    flex: none;
    width: 22px; height: 22px;
    border-radius: 50%;
    background: var(--on-blue);
  }
  .brand-name {
    font-size: 30px;
    letter-spacing: 1px;
    color: var(--on-blue);
    line-height: 1.1;
    white-space: nowrap;
  }
  .front-person {
    position: absolute;
    left: 96px; top: 196px;
    text-align: center;
  }
  .person-name {
    font-family: "Montserrat", Arial, sans-serif;
    font-weight: 700;
    font-size: 19px;
    letter-spacing: .5px;
    color: var(--on-blue);
  }
  .person-role {
    font-size: 15px;
    color: var(--on-blue-soft);
    margin-top: 2px;
  }

  /* Back */
  .card-back {
    background: var(--card-white);
    color: var(--ink);
    display: flex;
    padding: 34px 22px 28px 24px;
  }
  .back-identity {
    width: 236px;
    flex: none;
    display: flex;
    flex-direction: column;
    align-items: center;
    justify-content: center;
    text-align: center;
  }
  .back-brand {
    display: flex;
    align-items: center;
    gap: 8px;
    margin-bottom: 22px;
    white-space: nowrap;
  }
  .back-brand .brand-dot { background: var(--ink); width: 16px; height: 16px; }
  .back-brand .brand-name { color: var(--ink); font-size: 19px; letter-spacing: .3px; }
  .contact { font-size: 13px; line-height: 1.4; color: var(--ink); white-space: nowrap; }
  .contact strong { font-family: "Montserrat", Arial, sans-serif; font-size: 12px; }

  .appointments { flex: 1; padding-left: 16px; padding-top: 4px; }
  .appointments h2 {
    font-weight: 400;
    font-size: 16px;
    color: var(--ink);
    text-align: center;
    margin-bottom: 14px;
  }
  .appointment-list { list-style: none; }
  .appointment-slot {
    display: flex;
    align-items: baseline;
    gap: 4px;
    font-size: 12.5px;
    color: var(--ink-soft);
    height: 34px;
    white-space: nowrap;
  }
  .slot-line {
    display: inline-block;
    border-bottom: 1px solid var(--rule);
    height: 1px;
  }
  .slot-time { width: 18px; }
  .slot-detail { flex: 1; margin: 0 6px; }
  .slot-date { width: 16px; }
</style>
</head>
<body>
  <section class="card card-front" aria-label="Card front">
    <div class="front-brand">
      <span class="brand-dot"></span>
      <span class="brand-name">Marlow Naturopathics</span>
    </div>
    <div class="front-person">
      <p class="person-name">DENNIS MARLOW</p>
      <p class="person-role">Naturopath</p>
    </div>
  </section>

  <section class="card card-back" aria-label="Card back">
    <div class="back-identity">
      <div class="back-brand">
        <span class="brand-dot"></span>
        <span class="brand-name">Marlow Naturopathics</span>
      </div>
      <p class="contact">
        www.dennismarlowhealth-example.com<br>
        Level 1, 58 Torvane Street<br>
        Calder Bay NSW<br>
        <strong>T</strong> (02) 4391 7084
      </p>
    </div>
    <div class="appointments">
      <h2>Your Appointments</h2>
      <ol class="appointment-list">
        <li class="appointment-slot">1. <span class="slot-line slot-time"></span>am/pm <span class="slot-line slot-detail"></span><span class="slot-line slot-date"></span>/<span class="slot-line slot-date"></span>/<span class="slot-line slot-date"></span></li>
        <li class="appointment-slot">2. <span class="slot-line slot-time"></span>am/pm <span class="slot-line slot-detail"></span><span class="slot-line slot-date"></span>/<span class="slot-line slot-date"></span>/<span class="slot-line slot-date"></span></li>
        <li class="appointment-slot">3. <span class="slot-line slot-time"></span>am/pm <span class="slot-line slot-detail"></span><span class="slot-line slot-date"></span>/<span class="slot-line slot-date"></span>/<span class="slot-line slot-date"></span></li>
        <li class="appointment-slot">4. <span class="slot-line slot-time"></span>am/pm <span class="slot-line slot-detail"></span><span class="slot-line slot-date"></span>/<span class="slot-line slot-date"></span>/<span class="slot-line slot-date"></span></li>
        <li class="appointment-slot">5. <span class="slot-line slot-time"></span>am/pm <span class="slot-line slot-detail"></span><span class="slot-line slot-date"></span>/<span class="slot-line slot-date"></span>/<span class="slot-line slot-date"></span></li>
      </ol>
    </div>
  </section>
</body>
</html>
```